Determining number of boxes of planks of flooring for a room

Need a creative design of an infographic of a room with instructions on how to measure the room and use this measurement to determine how much flooring to order.
The floor planks come in boxes and each box has 36 planks. Each box covers 5 metre squared in total.
The intent of the infographic is to help inform the customer how many boxes they need to order for their room.
The infographic should match the style of flooring being sold (image provided) and the logo for the company (image provided).
A crude sketch of instructions to measure a room and determine the number of boxes is provided in a document attached with this brief. Need improvement to the steps mentioned in this document on the infographic created.

```html
<!DOCTYPE html>
<html lang="en">
<head>
<meta charset="utf-8">
<title>Flooring Pack Calculator</title>
<link rel="stylesheet" href="https://fonts.googleapis.com/css2?family=Montserrat:wght@300;400;500;600;700&display=swap">
<style>
  :root{
    --paper:#d7d3cd;
    --ink:#5b5246;
    --ink-soft:#6f665a;
    --text:#2b2824;
    --muted:#6c6760;
    --cell:#e6e2dc;
    --line:#9d958a;
    --art:#c9c3ba;
  }
  *{margin:0;padding:0;box-sizing:border-box}
  html,body{width:1200px;height:1200px;overflow:hidden;background:var(--paper)}
  body{font-family:"Montserrat",sans-serif;color:var(--text);position:relative}
  .abs{position:absolute}
  .corners{position:absolute;inset:0}
  .brand{position:absolute;top:66px;left:0;width:1200px;text-align:center}
  .brand-name{font-weight:300;font-size:52px;letter-spacing:3px;color:var(--ink);line-height:1;display:inline-flex;align-items:center;gap:16px}
  .brand-name .mark{width:18px;height:18px;background:var(--ink);display:inline-block}
  .brand-tag{font-size:14px;letter-spacing:5px;color:var(--ink);margin-top:6px;font-weight:400}
  .section-title{position:absolute;left:84px;font-size:30px;font-weight:400;letter-spacing:1px;color:var(--text)}
  .step{position:absolute;left:163px;display:flex;align-items:center;font-size:16px;color:var(--text)}
  .num{width:23px;height:23px;border-radius:50%;background:var(--ink);color:#eee9e1;font-size:13px;font-weight:600;display:flex;align-items:center;justify-content:center;margin-right:16px}
  .var{font-weight:500;font-size:20px;margin:0 18px 0 18px}
  .hint{color:var(--muted);font-size:15px}
  .formula{position:absolute;left:241px;width:144px;height:48px;border:1.5px solid var(--ink-soft);border-radius:6px;background:#e1ddd6;display:flex;align-items:center;justify-content:center;font-weight:600;font-size:26px;color:var(--text)}
  .note{position:absolute;left:268px;top:700px;width:245px;font-size:15.5px;line-height:1.25;color:var(--text)}
  .art{position:absolute;background:var(--art);border-radius:4px}
  .spec{position:absolute;left:578px;top:617px;border-collapse:separate;border-spacing:0;font-size:14px;text-align:center}
  .spec td,.spec th{border-right:1px solid var(--line);border-bottom:1px solid var(--line);background:var(--cell);height:27px;font-weight:400}
  .spec thead th{height:55px;font-weight:600;font-size:15px;border-top:1px solid var(--line)}
  .spec thead th small{display:block;font-weight:400;font-size:13px}
  .spec thead th.corner{background:transparent;border:none;border-right:1px solid var(--line);font-size:10px;font-weight:600;color:var(--ink);letter-spacing:1px}
  .spec thead th.packs{font-size:11.5px;line-height:1.2}
  .spec thead th.packs small{font-size:13px}
  .spec tbody th{font-size:11.5px;font-weight:600;border-left:1px solid var(--line)}
  .spec tbody tr:first-child th{border-top:1px solid var(--line);border-top-left-radius:6px}
  .spec tbody tr:last-child th{border-bottom-left-radius:6px}
  .spec thead th:last-child{border-top-right-radius:6px}
  .spec tbody tr:last-child td:last-child{border-bottom-right-radius:6px}
  .step-badge{position:absolute;width:28px;height:28px;border-radius:50%;background:var(--ink);color:#eee9e1;font-weight:600;font-size:15px;display:flex;align-items:center;justify-content:center}
  .mini-name{position:absolute;font-size:12px;font-weight:600;color:var(--ink);letter-spacing:1px}
</style>
</head>
<body>
  <svg class="corners" width="1200" height="1200" viewBox="0 0 1200 1200" aria-hidden="true">
    <g stroke="var(--ink)" stroke-width="3" fill="none">
      <path d="M29 130 V29 H130"/><path d="M1171 130 V29 H1070"/>
      <path d="M29 1070 V1171 H130"/><path d="M1171 1070 V1171 H1070"/>
    </g>
    <g fill="var(--ink)">
      <path d="M32 32 H88 L32 88 Z"/><path d="M1168 32 H1112 L1168 88 Z"/>
      <path d="M32 1168 H88 L32 1112 Z"/><path d="M1168 1168 H1112 L1168 1112 Z"/>
    </g>
  </svg>

  <header class="brand">
    <div class="brand-name"><span class="mark"></span>VERANTO</div>
    <div class="brand-tag">PREMIUM FLOORS AND TILES</div>
  </header>

  <h2 class="section-title" style="top:252px">RECTANGLE OR SQUARE ROOM?</h2>

  <div class="step" style="top:321px"><span class="num">1</span>measure<span class="var">a</span><span class="hint">(Room Length)</span></div>
  <div class="step" style="top:361px"><span class="num">2</span>measure<span class="var">b</span><span class="hint">(Room Width)</span></div>
  <div class="step" style="top:398px"><span class="num">3</span>Calculate<span class="var">C</span><span class="hint">(Room Size)</span></div>
  <div class="formula" style="top:444px">C = a×b</div>
  <div class="art" style="left:414px;top:458px;width:40px;height:20px" role="img" aria-label="Small floor tile icon"></div>

  <div class="step" style="top:533px"><span class="num">4</span>Calculate<span class="var">D</span><span class="hint">(Number of Packs)</span></div>
  <div class="formula" style="top:576px">D = C/5</div>
  <div class="art" style="left:413px;top:580px;width:42px;height:42px" role="img" aria-label="Stacked flooring packs icon"></div>

  <div class="step" style="top:664px"><span class="num">5</span>Round up<span class="var">D</span><span class="hint">(Number of Packs)</span></div>
  <div class="art" style="left:203px;top:718px;width:40px;height:42px" role="img" aria-label="Stacked flooring packs icon"></div>
  <p class="note">Always round up to the next integer to find out the actual number of packs you need to cover the floor</p>

  <div class="art" style="left:622px;top:340px;width:352px;height:200px" role="img" aria-label="Isometric floor slab labelled C with length a and width b dimension arrows"></div>
  <div class="art" style="left:975px;top:573px;width:38px;height:38px" role="img" aria-label="Stacked flooring packs icon"></div>

  <table class="spec">
    <thead>
      <tr>
        <th class="corner" style="width:90px">VERANTO</th>
        <th style="width:44px">a</th>
        <th style="width:45px">b</th>
        <th style="width:91px">C<small>(a×b)</small></th>
        <th style="width:89px">D<small>(C/5)</small></th>
        <th class="packs" style="width:117px">Number of packs<small>(round up D)</small></th>
      </tr>
    </thead>
    <tbody>
      <tr><th>Example 1</th><td>5</td><td>5</td><td>25</td><td>5</td><td>5</td></tr>
      <tr><th>Example 2</th><td>3</td><td>4</td><td>12</td><td>2.4</td><td>3</td></tr>
      <tr><th>Example 3</th><td>6</td><td>3</td><td>18</td><td>3.6</td><td>4</td></tr>
    </tbody>
  </table>

  <h2 class="section-title" style="top:860px">CUSTOM ROOM SHAPE?</h2>
  <div class="step" style="top:930px"><span class="num">1</span>Do a simple drawing</div>
  <div class="step" style="top:970px"><span class="num">2</span>Send it to us</div>
  <div class="step" style="top:1008px"><span class="num">3</span>We will be able to work it out for you</div>

  <div class="step-badge" style="left:654px;top:880px">1</div>
  <div class="step-badge" style="left:845px;top:880px">2</div>
  <div class="step-badge" style="left:1004px;top:880px">3</div>

  <div class="art" style="left:634px;top:940px;width:106px;height:95px" role="img" aria-label="Notepad with pencil"></div>

  <svg class="abs" style="left:800px;top:940px" width="110" height="95" viewBox="0 0 110 95" aria-hidden="true">
    <rect x="4" y="62" width="40" height="28" fill="none" stroke="var(--ink)" stroke-width="2"/>
    <path d="M4 62 L24 78 L44 62" fill="none" stroke="var(--ink)" stroke-width="2"/>
    <path d="M26 54 Q28 26 52 20" fill="none" stroke="var(--ink)" stroke-width="4"/>
    <path d="M46 12 L58 20 L46 28 Z" fill="var(--ink)"/>
  </svg>
  <div class="mini-name" style="left:862px;top:950px">VERANTO</div>

  <svg class="abs" style="left:990px;top:940px" width="80" height="40" viewBox="0 0 80 40" aria-hidden="true">
    <path d="M44 12 Q20 14 16 34" fill="none" stroke="var(--ink)" stroke-width="4"/>
    <path d="M8 30 L16 40 L24 30 Z" fill="var(--ink)"/>
  </svg>
  <div class="mini-name" style="left:1028px;top:950px">VERANTO</div>
  <div class="art" style="left:970px;top:998px;width:38px;height:38px" role="img" aria-label="Stacked flooring packs icon"></div>
</body>
</html>
```